Wholesale company needs a sales brochure for our latest gadget- Nimbo Pebble. We sell to retailers

We need a sale brochure for our new product- Nimbo/Dart Pebble. It's an elegant little device that connects to any smartphone using an APP and let you locate your keys or your phone when you can't find them. We would like to see a design that uses the colors: Light blue, Black and metallic silver. The final design should communicate tech and innovative product. We need a total of 4 pages of 8.5x11'' (US letter size) to describe:
- Product benefits
- Product in use
- Display solution
- Profit generator
- Success story

Attached below are photos of the packaging and the display for your reference. Better photos will be sent later.
Please keep in mind that this product should be displayed on the counter with high foot traffic OR hang on hooks on a display fixture in the store.

This brochure will be used mainly to be sent digitally via email BUT we will also print it and will be mailing copies to our buyers.

Target Market(s)

Retailers and Distributors.
Small to mid-size retail stores:
- Electronic stores
- Convenient store
- Cellphone stores
- Gift stores

Industry/Entity Type

Retail

Font styles to use
Sans Serif

Colors
0692cd
ffffff
f3f1f8
33a6d7
85cae6

Requirements
Must have
• Must have:
• - "techie" and innovative look to go hand in hand with the product itself.
• - "in use" photos
• - "Description of the product"
• - Spec info
Nice to have
• Pattern or abstract design on background behind the text and images

```html
<!DOCTYPE html>
<html lang="en">
<head>
<meta charset="utf-8">
<title>Nimbo Pebble — Sales Brochure</title>
<link rel="stylesheet" href="https://fonts.googleapis.com/css2?family=Open+Sans:ital,wght@0,400;0,600;0,700;1,400&display=swap">
<style>
  :root {
    --stage: #8f9094;
    --paper: #ffffff;
    --paper-shade: #f3f1f8;
    --ink: #232323;
    --ink-soft: #555a5f;
    --teal: #2a93a8;
    --cyan: #33a6d7;
    --sky: #85cae6;
    --magenta: #d8237d;
    --amber: #f4c21c;
  }
  * { box-sizing: border-box; margin: 0; padding: 0; }
  html, body { width: 1200px; height: 1025px; overflow: hidden; }
  body { background: var(--stage); font-family: "Open Sans", Arial, sans-serif; color: var(--ink); position: relative; }

  .spread { position: absolute; left: 73px; width: 1054px; height: 408px; background: var(--paper); overflow: hidden; }
  .spread--cover { top: 53px; }
  .spread--inside { top: 518px; }
  .spread__bg { position: absolute; inset: 0; width: 100%; height: 100%; }

  .abs { position: absolute; }
  .photo { position: absolute; border-radius: 6px; }
  .photo--tags { background: radial-gradient(circle at 60% 35%, #f2f2f2 0 22%, transparent 23%), linear-gradient(135deg, var(--magenta) 0 30%, var(--cyan) 30% 60%, #2b2b2b 60%); opacity: .9; }
  .photo--pack { background: linear-gradient(180deg, #2a2a2a 0 24%, #e9ecef 24% 100%); }
  .photo--stand { background: linear-gradient(180deg, #2a2a2a 0 18%, #e5e8eb 18% 84%, #2a2a2a 84%); }
  .pattern { position: absolute; background: linear-gradient(135deg, var(--magenta) 0%, var(--cyan) 45%, var(--amber) 100%); opacity: .85; }

  .brand { font-weight: 700; color: var(--ink); letter-spacing: -0.5px; line-height: 1; white-space: nowrap; }

  .contact { position: absolute; left: 24px; top: 322px; list-style: none; font-size: 13px; color: var(--ink); }
  .contact li { display: flex; align-items: center; gap: 8px; height: 22.5px; }
  .contact svg { width: 16px; height: 16px; }

  .bundle { position: absolute; right: 550px; top: 298px; text-align: right; }
  .bundle h2 { font-size: 22px; font-weight: 700; letter-spacing: .5px; margin-bottom: 8px; }
  .bundle p { font-size: 13px; font-weight: 600; line-height: 15.5px; }

  .features { position: absolute; left: 559px; top: 18px; list-style: none; }
  .features li { display: flex; align-items: center; gap: 12px; height: 51px; }
  .features .label { font-size: 12.5px; font-weight: 700; line-height: 14px; text-transform: uppercase; }
  .ico { width: 44px; height: 44px; border-radius: 50%; background: var(--teal); border: 3px solid #d9eef3; display: grid; place-items: center; }
  .ico svg { width: 22px; height: 22px; }

  .tagline { position: absolute; right: 14px; top: 84px; font-size: 26px; line-height: 32px; color: var(--teal); white-space: nowrap; }

  .perks { position: absolute; right: 20px; top: 364px; display: flex; align-items: center; gap: 8px; font-size: 9.5px; font-weight: 700; line-height: 11px; text-transform: uppercase; }
  .perks .sep { width: 1px; height: 28px; background: var(--ink); }
  .perks .badge { width: 24px; height: 24px; border-radius: 4px; background: var(--cyan); }
  .perks .group { display: flex; align-items: center; gap: 5px; }

  .heading { font-size: 20px; line-height: 26px; color: var(--teal); font-weight: 400; white-space: nowrap; }
  .body-copy { font-size: 9px; line-height: 10.8px; color: var(--ink); }
  .body-copy + .body-copy { margin-top: 10px; }

  .ribbon { display: inline-block; background: var(--teal); color: #fff; font-size: 11px; font-weight: 600; padding: 2px 14px 2px 8px; clip-path: polygon(0 0, 100% 0, 92% 100%, 0 100%); }

  .steps { list-style: none; margin-top: 16px; }
  .steps li { display: flex; align-items: flex-start; gap: 8px; font-size: 9px; line-height: 10.8px; min-height: 19px; }
  .steps .num { flex: none; width: 16px; height: 16px; background: var(--teal); color: #fff; font-size: 9px; display: grid; place-items: center; clip-path: polygon(0 0, 100% 50%, 0 100%); padding-right: 5px; }

  .howto { list-style: none; margin-top: 8px; }
  .howto li { display: flex; gap: 8px; align-items: flex-start; min-height: 31px; font-size: 9px; line-height: 10.8px; }
  .howto .ico { width: 28px; height: 28px; border-width: 2px; flex: none; }
  .howto .ico svg { width: 14px; height: 14px; }
  .howto .term { color: var(--cyan); }

  .mission { position: absolute; left: 548px; top: 324px; width: 250px; font-size: 8.4px; line-height: 10.8px; font-style: italic; color: var(--ink-soft); }
</style>
</head>
<body>

<svg width="0" height="0" style="position:absolute">
  <defs>
    <linearGradient id="wood" x1="0" y1="0" x2="1" y2="1">
      <stop offset="0" stop-color="#d3d7da"/><stop offset="1" stop-color="#9aa2a9"/>
    </linearGradient>
    <linearGradient id="fold" x1="0" x2="1">
      <stop offset="0" stop-color="#000" stop-opacity="0"/><stop offset=".5" stop-color="#000" stop-opacity=".12"/><stop offset="1" stop-color="#000" stop-opacity="0"/>
    </linearGradient>
    <symbol id="i-phone" viewBox="0 0 24 24"><rect x="7" y="2" width="10" height="20" rx="2" fill="none" stroke="#fff" stroke-width="2"/><circle cx="12" cy="18" r="1.2" fill="#fff"/></symbol>
    <symbol id="i-key" viewBox="0 0 24 24"><circle cx="9" cy="9" r="5" fill="none" stroke="#fff" stroke-width="2"/><path d="M12.5 12.5 20 20M17 17l2-2M15 15l2-2" stroke="#fff" stroke-width="2"/></symbol>
    <symbol id="i-camera" viewBox="0 0 24 24"><rect x="2" y="7" width="20" height="14" rx="2" fill="#fff"/><rect x="8" y="4" width="8" height="4" rx="1" fill="#fff"/><circle cx="12" cy="14" r="4" fill="#2a93a8"/><circle cx="12" cy="14" r="2.2" fill="#fff"/></symbol>
    <symbol id="i-pin" viewBox="0 0 24 24"><path d="M12 2a7 7 0 0 0-7 7c0 5 7 13 7 13s7-8 7-13a7 7 0 0 0-7-7z" fill="#fff"/><circle cx="12" cy="9" r="2.6" fill="#2a93a8"/></symbol>
  </defs>
</svg>

<!-- Outer spread: back cover + front cover -->
<section class="spread spread--cover">
  <svg class="spread__bg" viewBox="0 0 1054 408" preserveAspectRatio="none" aria-hidden="true">
    <polygon points="252,408 440,0 527,0 527,408" fill="url(#wood)"/>
    <polygon points="527,0 796,0 648,408 527,408" fill="url(#wood)"/>
    <rect x="512" y="0" width="30" height="408" fill="url(#fold)"/>
  </svg>

  <div class="photo photo--tags" style="left:30px;top:22px;width:250px;height:230px" role="img" aria-label="Three triangular tracker tags in white, pink, blue and black with a set of keys on a ring"></div>
  <div class="abs brand" style="left:18px;top:262px;font-size:32px">Nimbo Pebble</div>

  <ul class="contact">
    <li><svg viewBox="0 0 16 16"><circle cx="8" cy="8" r="8" fill="#33a6d7"/><rect x="6" y="4" width="4" height="8" rx="1" fill="#fff"/></svg>0100 555 0142</li>
    <li><svg viewBox="0 0 16 16"><circle cx="8" cy="8" r="8" fill="#33a6d7"/><rect x="4" y="5" width="8" height="6" fill="#fff"/><path d="M4 5l4 3 4-3" stroke="#33a6d7" fill="none"/></svg>info@nimbopebble.com</li>
    <li><svg viewBox="0 0 16 16"><circle cx="8" cy="8" r="8" fill="#33a6d7"/><circle cx="8" cy="8" r="4" fill="none" stroke="#fff"/><path d="M4 8h8M8 4v8" stroke="#fff"/></svg>nimbopebble.com</li>
  </ul>

  <div class="pattern" style="left:324px;top:0;width:205px;height:283px;clip-path:polygon(40% 0,100% 0,100% 100%,30% 80%,0 55%)" role="img" aria-label="Abstract cluster of overlapping translucent triangles in pink, cyan and yellow"></div>

  <div class="bundle">
    <h2>BUNDLE &amp; SAVE</h2>
    <p>Buy 3 get 1 FREE.<br>Just select from our bundled<br>options below for extreme savings!</p>
  </div>

  <ul class="features">
    <li><span class="ico"><svg><use href="#i-phone"/></svg></span><span class="label">Find your<br>phone</span></li>
    <li><span class="ico"><svg><use href="#i-key"/></svg></span><span class="label">Find your<br>keys</span></li>
    <li><span class="ico"><svg><use href="#i-camera"/></svg></span><span class="label">Selfie<br>remote</span></li>
    <li><span class="ico"><svg><use href="#i-pin"/></svg></span><span class="label">Lost<br>record</span></li>
  </ul>

  <div class="pattern" style="left:529px;top:219px;width:187px;height:189px;clip-path:polygon(0 0,60% 40%,100% 70%,70% 100%,0 100%)" role="img" aria-label="Abstract cluster of overlapping translucent triangles in pink, cyan and yellow"></div>

  <div class="abs brand" style="right:20px;top:24px;font-size:40px">Nimbo Pebble</div>
  <div class="tagline">Find your everything...</div>
  <div class="photo photo--tags" style="left:790px;top:136px;width:200px;height:206px" role="img" aria-label="Three triangular tracker tags stacked in white, pink, blue and black"></div>

  <div class="perks">
    <div class="group"><span style="text-align:right">Free app<br>LinkPod</span><span class="badge"></span></div>
    <span class="sep"></span>
    <div class="group"><span style="text-align:right">All major phones<br>compatible</span><span class="badge"></span><span class="badge" style="background:var(--sky)"></span></div>
    <span class="sep"></span>
    <div class="group"><span>Set up in<br>1 minute</span><span class="badge" style="width:16px;height:16px;border-radius:50%"></span></div>
  </div>
</section>

<!-- Inner spread: product description + how to use -->
<section class="spread spread--inside">
  <svg class="spread__bg" viewBox="0 0 1054 408" preserveAspectRatio="none" aria-hidden="true">
    <polygon points="0,0 268,0 0,330" fill="url(#wood)"/>
    <polygon points="872,0 1054,0 1054,408 776,408" fill="url(#wood)"/>
    <rect x="512" y="0" width="30" height="408" fill="url(#fold)"/>
  </svg>

  <div class="photo photo--pack" style="left:18px;top:14px;width:100px;height:200px" role="img" aria-label="Hanging retail blister pack showing a tracker tag with keys"></div>
  <div class="photo photo--tags" style="left:150px;top:12px;width:140px;height:126px" role="img" aria-label="Three triangular tracker tags in white, pink, blue and black"></div>
  <div class="pattern" style="left:0;top:218px;width:184px;height:190px;clip-path:polygon(0 0,40% 30%,100% 70%,90% 100%,0 100%)" role="img" aria-label="Abstract cluster of overlapping translucent triangles in pink, cyan and yellow"></div>

  <div class="abs" style="left:206px;top:146px;width:300px">
    <h2 class="heading">Find your phone, Find your keys</h2>
    <p class="body-copy" style="margin-top:5px">Track the things that matter to you most with our Bluetooth Finder. Just attach it to your keys, pair it with our intuitive app and viola! Lost is now FOUND.</p>
    <p class="body-copy">Nimbo Pebble is a Bluetooth item finder. That means that you can attach it to any valuable you own and ring it in seconds with the LinkPod Application on your phone. In addition, you can double press the Pebble and your phone will ring!</p>
  </div>

  <div class="abs" style="left:206px;top:280px;width:300px">
    <span class="ribbon">GETTING STARTED:</span>
    <ol class="steps">
      <li><span class="num">1</span><span>Download the free “LinkPod” app</span></li>
      <li><span class="num">2</span><span>Turn on the device with a long press</span></li>
      <li><span class="num">3</span><span>Open the app and press the “+” icon then selecect<br><b>Nimbo Pebble</b> device to pair</span></li>
    </ol>
  </div>

  <div class="abs brand" style="left:548px;top:92px;font-size:38px">Nimbo Pebble</div>

  <div class="abs" style="left:527px;top:150px;width:290px">
    <span class="ribbon" style="padding-left:22px">HAW TO USE:</span>
    <ul class="howto" style="padding-left:21px">
      <li><span class="ico"><svg><use href="#i-phone"/></svg></span><span><span class="term">To locate your phone:</span> Double press the <b>pebble</b> to activate the alarm</span></li>
      <li><span class="ico"><svg><use href="#i-key"/></svg></span><span><span class="term">To find your keys:</span> Navigate to the “Device” tab and press the “Call” button</span></li>
      <li><span class="ico"><svg><use href="#i-camera"/></svg></span><span><span class="term">Selfie Remote:</span> Navigate to the “Camera” tab in the app and single press the <b>pebble</b> to take a picture</span></li>
      <li><span class="ico"><svg><use href="#i-pin"/></svg></span><span><span class="term">Lost Record:</span> Navigate to the “Location” tab and press the “Lost Record” button to find the last location the device was disconnected on the map</span></li>
    </ul>
  </div>

  <p class="mission">We believe in finding lost things. After countless hours of research, we have created something we think every person can use. We hope to eliminate the frustration and confusion felt by the loss of a phone, keys or any other important item. Our mission is to give you the power to find every anything and everything all the time.</p>

  <div class="pattern" style="left:760px;top:2px;width:248px;height:148px;clip-path:polygon(0 30%,40% 0,100% 0,80% 60%,40% 100%)" role="img" aria-label="Abstract cluster of overlapping translucent triangles in pink, cyan and yellow"></div>
  <div class="photo photo--stand" style="left:840px;top:66px;width:180px;height:316px" role="img" aria-label="Counter display stand filled with packaged tracker tags"></div>
</section>

</body>
</html>
```